Appraisal and Umpire Services for Property Damage Insurance Claims

I need a banner design that I can post as an advertisement on industry web pages. I would like this to be elegant and reflective of quality, integrity and professionalism.

Target Market(s)

Insurance Companies and Attorneys

Industry/Entity Type

Insurance

Contact Information for Business Card

Gerald M. Hollis
918 Birchwell Lane
PO Box 582
Clifton Park, NY 12093
ghollis@brindlevault.com
Phone: (800) 555-0147, Ext. 2861
Direct: (315) 555-0189

Logo Text

Line One: Velmar Brook Claim Service, Inc. Line two: Appraisal and Umpire Services

Font styles to use
Serif
Sans Serif

Colors
0255a3
f78f20
faa54b
3176b5

Requirements
Must have
• New Logo and matching banner, business card and stationary.
• The colors must be orange and navy blue in the logo. I have selected them below.

```html
<!DOCTYPE html>
<html lang="en">
<head>
<meta charset="utf-8">
<title>Velmar Brook Claim Service – Banner</title>
<link href="https://fonts.googleapis.com/css2?family=Roboto+Condensed:wght@400;500;700&family=Roboto:wght@400;500&display=swap" rel="stylesheet">
<style>
  :root {
    --navy: #22285e;
    --blue: #0255a3;
    --orange: #f78f20;
    --orange-light: #faa54b;
    --ink: #2b2b2b;
    --panel: #f4f4f4;
    --white: #ffffff;
  }
  html, body {
    margin: 0;
    padding: 0;
    width: 1200px;
    height: 309px;
    overflow: hidden;
    background: var(--white);
  }
  .banner {
    position: relative;
    width: 1200px;
    height: 309px;
    overflow: hidden;
    font-family: "Roboto", Arial, sans-serif;
  }
  .banner-shapes {
    position: absolute;
    inset: 0;
  }
  .brand {
    position: absolute;
    left: 28px;
    top: 118px;
    color: var(--navy);
    font-family: "Roboto Condensed", Arial, sans-serif;
    font-weight: 700;
    line-height: 1;
  }
  .brand-name {
    font-size: 41px;
    letter-spacing: 0.5px;
    display: block;
  }
  .brand-sub {
    font-size: 22px;
    letter-spacing: 2.4px;
    display: block;
    margin-top: 6px;
  }
  .message {
    position: absolute;
    left: 440px;
    width: 320px;
    top: 64px;
    text-align: center;
  }
  .message-kicker {
    margin: 0;
    font-family: "Roboto Condensed", Arial, sans-serif;
    font-weight: 500;
    font-size: 22px;
    color: var(--navy);
    letter-spacing: 0.2px;
  }
  .message-title {
    margin: 8px 0 0;
    font-family: "Roboto Condensed", Arial, sans-serif;
    font-weight: 700;
    font-size: 36px;
    color: var(--blue);
    letter-spacing: 0.4px;
  }
  .message-rule {
    width: 292px;
    height: 1px;
    background: var(--ink);
    margin: 14px auto 12px;
    border: 0;
  }
  .message-body {
    margin: 0;
    font-size: 15.5px;
    line-height: 1.5;
    color: var(--ink);
  }
  .cta {
    display: inline-block;
    margin-top: 20px;
    width: 160px;
    padding: 13px 0;
    border: 2px solid var(--blue);
    border-radius: 12px;
    color: var(--blue);
    font-family: "Roboto Condensed", Arial, sans-serif;
    font-weight: 500;
    font-size: 16px;
    text-decoration: none;
    background: var(--white);
  }
</style>
</head>
<body>
  <div class="banner">
    <svg class="banner-shapes" width="1200" height="309" viewBox="0 0 1200 309" aria-hidden="false">
      <defs>
        <linearGradient id="wall-tone" x1="0" y1="0" x2="1" y2="1">
          <stop offset="0" stop-color="#e4e1de"/>
          <stop offset="0.5" stop-color="#f3f1ef"/>
          <stop offset="1" stop-color="#dcd8d4"/>
        </linearGradient>
        <linearGradient id="hands-tone" x1="0" y1="0" x2="1" y2="1">
          <stop offset="0" stop-color="#2e3a4e"/>
          <stop offset="0.45" stop-color="#c9a58f"/>
          <stop offset="0.7" stop-color="#c8473d"/>
          <stop offset="1" stop-color="#24303f"/>
        </linearGradient>
        <linearGradient id="panel-tone" x1="0" y1="0" x2="1" y2="0">
          <stop offset="0" stop-color="#ffffff"/>
          <stop offset="1" stop-color="#eeeeee"/>
        </linearGradient>
      </defs>
      <rect class="wall-photo" x="250" y="0" width="700" height="309" fill="url(#wall-tone)" role="img" aria-label="Cracked brick wall background photo"/>
      <polygon class="side-panel" points="0,0 345,0 360,154 258,309 0,309" fill="url(#panel-tone)"/>
      <polygon class="navy-chevron" points="345,0 388,0 402,154 303,309 258,309 360,154" fill="var(--navy)"/>
      <polygon class="hands-photo" points="790,0 1200,0 1200,309 760,309 880,155" fill="url(#hands-tone)" role="img" aria-label="Photo of hands sheltering a small red model house with cracks"/>
      <polygon class="orange-stripe" points="742,0 790,0 880,155 858,155" fill="var(--orange-light)"/>
    </svg>

    <div class="brand">
      <span class="brand-name">VELMAR BROOK</span>
      <span class="brand-sub">CLAIM SERVICE, INC</span>
    </div>

    <div class="message">
      <p class="message-kicker">WE ARE RESPONSIBLE FOR YOUR</p>
      <h1 class="message-title">DAMAGE PROPERTY</h1>
      <hr class="message-rule">
      <p class="message-body">Contrary to popular belief, Lorem Ipsum is not simply random text. It has roots in a</p>
      <a class="cta" href="#">LEARN MORE</a>
    </div>
  </div>
</body>
</html>
```